New Summit Tile Billboard at HQ

Looking to design a catchy image / theme for a billboard located just above our corporate HQ showroom and warehouse, along the service road of a 6-lane highway. Billboard measures 8ft x 24 ft. Would like to highlight that the store location is directly beneath the sign.

We are a retail and wholesale business selling premium flooring, ready to assemble cabinets, and granite countertops. See image ideas attached. Our information:
NAME: Summit Tile, Cabinets, Countertops
ADDRESS: 417 W. Hwy 82, Duncanville, TX 75284
WEBSITE: www.summittilehub.example
PHONE: 972-8-TILEUP (972-845-3887)

```html
<!DOCTYPE html>
<html lang="en">
<head>
<meta charset="utf-8">
<title>Summit Tile Billboard</title>
<link href="https://fonts.googleapis.com/css2?family=Montserrat:wght@500;700;800&display=swap" rel="stylesheet">
<style>
  :root {
    --green: #5f993d;
    --lime: #8cc63f;
    --black: #0b0b0b;
    --gray: #dcdcdc;
    --white: #ffffff;
    --ink: #111111;
    --page: #f2f2f2;
  }
  * { margin: 0; padding: 0; box-sizing: border-box; }
  html, body { width: 1200px; height: 1200px; overflow: hidden; background: var(--page); }
  body { font-family: "Montserrat", sans-serif; }

  .billboard {
    position: absolute; left: 0; top: 400px;
    width: 1200px; height: 400px;
    background: var(--green);
    overflow: hidden;
  }

  /* top info strip */
  .brand-tab {
    position: absolute; left: 0; top: 0; width: 270px; height: 100px;
    background: var(--gray);
    display: flex; align-items: center; padding-left: 26px;
  }
  .brand-name {
    font-weight: 800; font-size: 30px; color: var(--ink); letter-spacing: -0.5px; white-space: nowrap;
  }
  .contact-bar {
    position: absolute; left: 250px; top: 0; right: 0; height: 100px;
    background: var(--black);
    border-bottom-left-radius: 40px;
    display: flex; align-items: center; justify-content: flex-end;
    gap: 12px; padding: 0 24px 0 40px;
    color: var(--white); font-weight: 500; font-size: 20px; white-space: nowrap;
  }
  .contact-bar svg { width: 22px; height: 22px; flex: none; }
  .contact-bar .divider { font-weight: 700; }
  .contact-bar .web { font-weight: 800; font-size: 26px; }
  .contact-bar .web .accent { color: var(--lime); }

  /* services */
  .service {
    position: absolute; display: flex; align-items: center; gap: 12px;
    color: var(--white); font-weight: 800; line-height: 1; white-space: nowrap;
    letter-spacing: -1px;
  }
  .service svg { flex: none; }
  .service--floors { left: 28px; top: 122px; font-size: 62px; }
  .service--cabinets { left: 650px; top: 112px; font-size: 72px; }
  .service--countertops { left: 28px; top: 208px; font-size: 62px; }

  .perks {
    position: absolute; left: 672px; top: 204px;
    list-style: none; color: var(--ink); font-weight: 800; font-size: 22px; line-height: 34px;
    white-space: nowrap;
  }
  .perks li::before {
    content: ""; display: inline-block; width: 10px; height: 10px;
    background: var(--ink); margin-right: 12px; vertical-align: middle;
  }

  /* bottom address strip */
  .address-bar {
    position: absolute; left: 0; bottom: 0; width: 970px; height: 90px;
    background: var(--black); border-top-right-radius: 40px;
    display: flex; align-items: center; padding-left: 40px;
    color: var(--white); font-weight: 800; font-size: 40px; letter-spacing: -1px; white-space: nowrap;
  }
  .store-panel {
    position: absolute; right: 0; bottom: 0; width: 260px; height: 100px;
    background: var(--gray);
  }
  .below-marker {
    position: absolute; left: 968px; top: 284px; width: 110px; height: 110px;
  }
</style>
</head>
<body>
  <section class="billboard">
    <div class="brand-tab"><span class="brand-name">Summit Tile</span></div>

    <header class="contact-bar">
      <svg viewBox="0 0 24 24" fill="none" stroke="var(--lime)" stroke-width="2" aria-hidden="true">
        <path d="M5 3h4l2 5-2.5 1.5a11 11 0 0 0 6 6L16 13l5 2v4a2 2 0 0 1-2 2A16 16 0 0 1 3 5a2 2 0 0 1 2-2z"/>
      </svg>
      <span class="phone">972-8-TILEUP <strong>(972-845-3887)</strong></span>
      <span class="divider">|</span>
      <svg viewBox="0 0 24 24" fill="none" stroke="var(--lime)" stroke-width="1.8" aria-hidden="true">
        <circle cx="12" cy="12" r="10"/><path d="M2 12h20M12 2c3 3 3 17 0 20M12 2c-3 3-3 17 0 20"/>
      </svg>
      <span class="web">WWW.<span class="accent">SUMMITTILEHUB</span>.EXAMPLE</span>
    </header>

    <div class="service service--floors">
      <svg width="40" height="40" viewBox="0 0 40 40" aria-hidden="true"><rect x="3" y="9" width="28" height="28" fill="none" stroke="var(--black)" stroke-width="4"/><path d="M9 22l7 8 20-26" fill="none" stroke="var(--white)" stroke-width="5"/></svg>
      SUMMIT TILE
    </div>
    <div class="service service--cabinets">
      <svg width="48" height="48" viewBox="0 0 40 40" aria-hidden="true"><rect x="3" y="9" width="28" height="28" fill="none" stroke="var(--black)" stroke-width="4"/><path d="M9 22l7 8 20-26" fill="none" stroke="var(--white)" stroke-width="5"/></svg>
      CABINETS
    </div>
    <div class="service service--countertops">
      <svg width="40" height="40" viewBox="0 0 40 40" aria-hidden="true"><rect x="3" y="9" width="28" height="28" fill="none" stroke="var(--black)" stroke-width="4"/><path d="M9 22l7 8 20-26" fill="none" stroke="var(--white)" stroke-width="5"/></svg>
      COUNTERTOPS
    </div>

    <ul class="perks">
      <li>BEST PRICES ON THE MARKET PERIOD</li>
      <li>FREE IN HOME CONSULTATION</li>
    </ul>

    <div class="store-panel"></div>
    <div class="address-bar">417 W. HWY 82, DUNCANVILLE, TX 75284</div>

    <svg class="below-marker" viewBox="0 0 130 130" role="img" aria-label="Arrow pointing down to the store">
      <circle cx="65" cy="65" r="60" fill="var(--white)" stroke="var(--green)" stroke-width="7"/>
      <circle cx="65" cy="65" r="64" fill="none" stroke="var(--black)" stroke-width="2"/>
      <path d="M48 22h34v44h20L65 110 28 66h20z" fill="var(--white)" stroke="var(--green)" stroke-width="5" stroke-linejoin="round"/>
    </svg>
  </section>
</body>
</html>
```